Printing Business Card

I would like the colorful accents of my business to match with an artistic design. The idea is that I would like to have a creative mix so that I am making a embossed, suede card to show off with marketing events.

```html
<!DOCTYPE html>
<html lang="en">
<head>
<meta charset="utf-8">
<title>Keystone Print Co. – Business Card</title>
<link rel="stylesheet" href="https://fonts.googleapis.com/css2?family=Poppins:wght@400;500&display=swap">
<style>
  :root {
    --backdrop: #d8d2ca;
    --card-top: #f4f3f1;
    --card-bottom: #e6e3df;
    --ink: #1c1c1e;
    --brand-blue: #1f6fd1;
    --brand-magenta: #d0266f;
    --brand-yellow: #e0a81f;
    --brand-black: #141416;
  }
  * { box-sizing: border-box; margin: 0; padding: 0; }
  html, body {
    width: 1200px; height: 970px; overflow: hidden;
    background: var(--backdrop);
    font-family: "Poppins", sans-serif;
    color: var(--ink);
  }
  .card {
    position: absolute; left: 60px; top: 176px;
    width: 1080px; height: 618px;
    background: linear-gradient(160deg, var(--card-top), var(--card-bottom));
    box-shadow: 0 18px 40px rgba(0,0,0,0.18);
    overflow: hidden;
  }
  .brand {
    position: absolute; left: 60px; top: 262px; width: 420px;
    display: flex; align-items: center; justify-content: center; gap: 16px;
  }
  .brand-dot {
    width: 40px; height: 40px; border-radius: 50%;
    background: var(--brand-magenta); flex: none;
  }
  .brand-name {
    font-size: 36px; font-weight: 500; color: var(--ink); white-space: nowrap;
  }
  .divider {
    position: absolute; left: 514px; top: 168px;
    width: 2px; height: 290px; background: var(--ink);
  }
  .details { position: absolute; left: 598px; top: 166px; }
  .person-name { font-size: 33px; font-weight: 500; line-height: 1.05; letter-spacing: 0.3px; }
  .person-role { font-size: 26px; font-weight: 400; line-height: 1.2; }
  .address { margin-top: 26px; font-size: 26px; line-height: 1.24; }
  .contacts { margin-top: 26px; list-style: none; }
  .contacts li {
    display: flex; align-items: center; gap: 16px;
    font-size: 26px; line-height: 35px;
  }
  .contacts svg { width: 24px; height: 24px; flex: none; }
  .colour-bar {
    position: absolute; left: 0; bottom: 0; width: 100%; height: 14px; display: flex;
  }
  .colour-bar span { height: 100%; }
  .bar-blue { width: 156px; background: var(--brand-blue); }
  .bar-magenta { width: 152px; background: var(--brand-magenta); }
  .bar-yellow { width: 155px; background: var(--brand-yellow); }
  .bar-black { flex: 1; background: var(--brand-black); }
</style>
</head>
<body>
  <section class="card">
    <div class="brand">
      <span class="brand-dot"></span>
      <span class="brand-name">Keystone Print Co.</span>
    </div>

    <div class="divider"></div>

    <div class="details">
      <h1 class="person-name">DANIEL REEVE</h1>
      <p class="person-role">Director</p>
      <p class="address">PO BOX 456, Harbour Lane<br>5th street, Ashford</p>
      <ul class="contacts">
        <li>
          <svg viewBox="0 0 24 24" aria-hidden="true"><path fill="#1c1c1e" d="M6.6 3.2 9 2.5l1.6 4.6-2 1.2c.8 2.8 2.6 5.2 5 6.8l1.6-1.7 4.3 2.3-.9 2.4c-.4 1-1.5 1.6-2.6 1.3C9.6 18 5.1 12.4 4.6 6c-.1-1.2.8-2.4 2-2.8z"/></svg>
          +1 555 204 318
        </li>
        <li>
          <svg viewBox="0 0 24 24" aria-hidden="true"><rect x="2" y="5" width="20" height="14" fill="#1c1c1e"/><path d="M2.5 5.5 12 13l9.5-7.5" fill="none" stroke="#f1efec" stroke-width="1.6"/></svg>
          hello@keystoneprint.com
        </li>
        <li>
          <svg viewBox="0 0 24 24" aria-hidden="true"><g fill="none" stroke="#1c1c1e" stroke-width="1.6"><circle cx="12" cy="12" r="10" fill="#1c1c1e"/><ellipse cx="12" cy="12" rx="4.5" ry="10" stroke="#f1efec"/><path d="M2 12h20M4 7h16M4 17h16" stroke="#f1efec"/></g></svg>
          www.keystoneprint.com
        </li>
      </ul>
    </div>

    <div class="colour-bar">
      <span class="bar-blue"></span>
      <span class="bar-magenta"></span>
      <span class="bar-yellow"></span>
      <span class="bar-black"></span>
    </div>
  </section>
</body>
</html>
```